Brenwick Homes Realty is seeking to have his informational, lead capture and Internet presence website

white and blue would be prevailed colors with scenarios of Los Angeles icons: Hollywood sign, Santa Monica pier and other beaches with palm trees. It should include information For Buyers, as well as For Sellers; common terminology in the process of purchase and selling houses and basic steps in the process of purchasing and/or selling a house.
Scroll down type of website is prefer, but tabs would be acceptable. Tabs:
About Us. For Buyers. For Sellers, Contact Us.
Links to: Terminology; process of purchase; process of selling.
Updates

Target Market(s)

Mainly focus on BUYERS.

Industry/Entity Type

California Real Estate

Coding

Coded - Design and coding required

Number of Pages Required

3 page

Colors
0054AA
0677BA
7BADD7
CADEEF
E8F1F8

Requirements
Must have
• a slogan under Brenwick Homes Realty: "Southern California Specialists Since 2004". Houses pictures must be Craftman, Country, or Ranch, but no
Nice to have
• On the first page, ABOUT US should be as a map of where to find what visitor needs: For Buyers ( description and link to2nd Page) including at the end description of the process. On 1st page also services offered For Sellers (description of what we do, -3rd page- and at the bottom, process of purchasing). Pages 2 and 3 might need a link to Terminology that will describe used terms. I see my website having at the bottom of every page with my CONTACT US information as well as invitation to send visitor's info to get personalize service. ALSO need as a legal disclaimer licenses numbers and Regulator. (To be provided to winner)
Should not have
• Listings

```html
<!DOCTYPE html>
<html lang="en">
<head>
<meta charset="utf-8">
<title>Brenwick Homes Realty</title>
<link href="https://fonts.googleapis.com/css2?family=Poppins:wght@300;400;500;600;700;800&display=swap" rel="stylesheet">
<style>
:root{
  --blue:#0054AA;
  --blue-mid:#0677BA;
  --blue-soft:#7BADD7;
  --blue-pale:#CADEEF;
  --blue-mist:#E8F1F8;
  --section-tint:#EEF3F9;
  --ink:#1d1d1f;
  --text:#3a3a3a;
  --white:#ffffff;
  --dark:#2a2f36;
}
*{margin:0;padding:0;box-sizing:border-box}
html,body{width:1200px;height:4345px;overflow:hidden}
body{position:relative;font-family:"Poppins",sans-serif;color:var(--text);background:var(--white)}
.abs{position:absolute}
a{color:inherit;text-decoration:none}

/* top bar & header */
.topbar{left:0;top:0;width:1200px;height:34px;background:var(--blue)}
.topbar-license{right:162px;top:8px;font-size:12px;font-weight:600;color:var(--white);letter-spacing:.3px}
.site-header{left:0;top:34px;width:1200px;height:77px;background:var(--white)}
.brand{display:flex;align-items:center;gap:9px}
.brand-dot{width:22px;height:22px;border-radius:50%;background:var(--blue)}
.brand-name{font-size:15px;font-weight:600;color:var(--blue);letter-spacing:.5px;line-height:1}
.header-brand{left:160px;top:28px}
.main-nav{left:0;top:0;width:1200px;height:77px}
.main-nav a{position:absolute;top:30px;font-size:13px;font-weight:500;color:var(--ink)}
.main-nav a.active{color:var(--blue)}
.nav-contact{left:932px !important;top:22px !important;width:106px;height:34px;border:1.5px solid var(--blue);border-radius:17px;display:flex;align-items:center;justify-content:center;color:var(--blue) !important}

/* hero */
.hero{left:0;top:111px;width:1200px;height:600px;background:linear-gradient(180deg,#9c7e9c 0%,#c79a9e 35%,#8a8497 62%,#4f5a6c 100%)}
.hero-title{left:160px;top:258px;font-size:55px;font-weight:800;color:var(--white);line-height:58px;letter-spacing:.5px}
.hero-slogan{left:161px;top:390px;font-size:19px;font-weight:400;color:var(--white)}
.btn{display:flex;align-items:center;justify-content:center;gap:6px;border-radius:22px;font-size:14px;font-weight:500}
.btn-buyers{left:162px;top:439px;width:140px;height:42px;background:var(--blue);color:var(--white)}
.btn-sellers{left:319px;top:439px;width:140px;height:42px;background:var(--blue-soft);color:var(--white)}
.hero-wave{left:0;top:540px;width:1200px;height:171px}

/* intro */
.section-title{width:1200px;left:0;text-align:center;font-size:26px;color:var(--ink);letter-spacing:.3px}
.section-title b{font-weight:700}
.section-title span{font-weight:400}
.title-wave{left:556px;width:88px;height:20px}
.intro-title{top:775px;font-weight:700}
.intro-lead{left:180px;top:857px;width:840px;text-align:center;font-size:14.5px;font-weight:600;color:var(--ink);line-height:22px}
.body-copy{left:160px;width:880px;text-align:center;font-size:12.8px;line-height:23px;color:var(--text);z-index:2}
.intro-copy{left:165px;width:870px;top:917px}
.hollywood-photo{left:0;top:975px;width:1200px;height:354px;z-index:1;background:linear-gradient(180deg,rgba(255,255,255,0) 0%,#f1f3f6 18%,#dfe4ea 32%,#b6a58a 58%,#8a6a45 80%,#6a4e32 100%)}

/* buyers */
.buyers-title{top:1394px}
.buyers-copy{left:190px;width:820px;top:1477px}
.process-title{font-size:26px;color:var(--ink)}
.process-title span{font-weight:400}
.process-title b{font-weight:700}
.buyers-process-title{left:733px;top:1573px}
.photo-circle{border-radius:50%}
.buyers-photo{left:179px;top:1656px;width:412px;height:412px;background:linear-gradient(160deg,#eef0f2 0%,#c9ced6 45%,#7e8a9c 100%)}
.step-line{width:0;border-left:1px solid var(--blue-pale)}
.step-dot{position:absolute;width:12px;height:12px;border-radius:50%;border:2px solid var(--blue-soft);background:var(--white)}
.step-dot::after{content:"";position:absolute;left:2px;top:2px;width:4px;height:4px;border-radius:50%;background:var(--blue)}
.step-icon{position:absolute;width:60px;height:60px;border-radius:50%;background:var(--blue);box-shadow:0 0 0 4px var(--blue-mist)}
.step-icon svg{position:absolute;left:15px;top:15px}
.step-label{position:absolute;font-size:13.5px;font-weight:600;color:var(--ink);letter-spacing:.6px;white-space:nowrap}
.btn-outline{width:148px;height:42px;border:1.5px solid var(--blue);border-radius:21px;color:var(--blue);background:var(--white)}
.buyers-more{left:525px;top:2213px}

/* sellers */
.sellers-band{left:0;top:2331px;width:1200px;height:979px;background:var(--section-tint)}
.sellers-title{top:2398px}
.sellers-copy{left:160px;width:880px;top:2481px}
.sellers-process-title{left:211px;top:2586px}
.sellers-photo{left:609px;top:2672px;width:412px;height:412px;background:linear-gradient(160deg,#e9ece8 0%,#b7c0b2 45%,#5c6a5a 100%)}
.sellers-more{left:525px;top:3190px}

/* contact */
.contact-band{left:0;top:3310px;width:1200px;height:650px;background:linear-gradient(180deg,#31363d 0%,#3b3a3c 40%,#4a3c36 70%,#2e3238 100%)}
.contact-heading{font-size:26px;color:var(--white)}
.contact-heading span{font-weight:400}
.contact-heading b{font-weight:700}
.reply-heading{left:160px;top:3375px}
.reply-note{left:162px;top:3419px;font-size:13px;color:var(--white)}
.field{left:160px;width:399px;border:1px solid rgba(255,255,255,.85);border-radius:4px;padding:11px 13px;font-size:11.5px;color:var(--white);font-family:inherit}
.field-name{top:3460px;height:40px}
.field-email{top:3514px;height:40px}
.field-phone{top:3567px;height:40px}
.field-message{top:3619px;height:100px}
.btn-submit{left:162px;top:3744px;width:118px;height:42px;background:var(--blue);color:var(--white)}
.us-heading{left:645px;top:3375px}
.contact-line{left:645px;display:flex;align-items:flex-start;gap:14px;color:var(--white);font-size:13px;line-height:22px}
.contact-address{top:3434px}
.contact-phone{top:3492px;font-size:17px;font-weight:600;letter-spacing:.5px}
.contact-email{top:3534px}
.map-frame{left:641px;top:3580px;width:397px;height:206px;border:4px solid var(--white);background:linear-gradient(135deg,#cfe3c8 0%,#e8eedd 45%,#bfd6ea 100%)}
.contact-wave{left:0;top:3810px;width:1200px;height:150px}

/* footer */
.site-footer{left:0;top:3960px;width:1200px;height:385px;background:linear-gradient(180deg,#ffffff 0%,#f4f6f8 100%)}
.footer-brand{left:160px;top:4070px}
.footer-tag{left:160px;top:4147px;font-size:10px;font-weight:600;color:var(--ink)}
.footer-legal{left:162px;top:4168px;width:440px;font-size:9.6px;line-height:17px;color:var(--text)}
.footer-links a{position:absolute;font-size:12px;color:var(--text)}
.footer-links a.active{color:var(--blue)}
.copyright{left:160px;top:4310px;font-size:12px;color:var(--text)}
.legal-links{right:162px;top:4310px;font-size:12px;color:var(--text)}
</style>
</head>
<body>

<div class="abs topbar"></div>
<div class="abs topbar-license">CA DRE #01739254</div>

<header class="abs site-header">
  <div class="abs brand header-brand"><span class="brand-dot"></span><span class="brand-name">BRENWICK HOMES REALTY</span></div>
  <nav class="abs main-nav">
    <a class="active" style="left:527px">Home</a>
    <a style="left:609px">About Us</a>
    <a style="left:711px">For Buyers</a>
    <a style="left:822px">For Sellers</a>
    <a class="nav-contact">Contact Us</a>
  </nav>
</header>

<section class="abs hero" role="img" aria-label="Los Angeles skyline at dusk framed by tall palm trees"></section>
<h1 class="abs hero-title">BRENWICK<br>HOMES REALTY</h1>
<p class="abs hero-slogan">Southern California Specialists Since 2004</p>
<a class="abs btn btn-buyers">For Buyers <svg width="8" height="10" viewBox="0 0 8 10"><path d="M2 1l4 4-4 4" fill="none" stroke="#fff" stroke-width="1.6"/></svg></a>
<a class="abs btn btn-sellers">For Sellers <svg width="8" height="10" viewBox="0 0 8 10"><path d="M2 1l4 4-4 4" fill="none" stroke="#fff" stroke-width="1.6"/></svg></a>
<svg class="abs hero-wave" viewBox="0 0 1200 171" preserveAspectRatio="none">
  <path d="M0 30 C160 140 380 175 640 120 C860 70 1040 40 1200 110 L1200 171 L0 171 Z" fill="var(--blue)"/>
  <path d="M0 70 C170 165 400 190 650 140 C870 95 1050 90 1200 150 L1200 171 L0 171 Z" fill="#fff"/>
</svg>

<div class="abs hollywood-photo" role="img" aria-label="Hollywood hillside with the famous sign under a hazy sky"></div>
<h2 class="abs section-title intro-title">BRENWICK HOMES REALTY</h2>
<svg class="abs title-wave" style="top:820px" viewBox="0 0 88 20"><path d="M2 12 C22 2 44 4 60 8 C70 10 80 9 86 5" fill="none" stroke="var(--blue)" stroke-width="3"/><path d="M8 17 C28 9 48 11 62 14 C72 15 80 14 84 12" fill="none" stroke="var(--blue-mid)" stroke-width="2"/></svg>
<p class="abs intro-lead">Sylmar ...is a ranch style community with large lots and horse properties. Sylmar is a suburban neighborhood in the San Fernando Valley which includes:</p>
<p class="abs body-copy intro-copy">Northridge, Tarzana, Encino, Woodland Hills, Granada Hills, Mission Hills, Reseda, Van Nuys, and is the northernmost neighborhood within the City of Los Angeles. I moved to Sylmar in 1985 because we saw the cities potential to grow, where I formed Brenwick Homes Realty in 2006.</p>

<h2 class="abs section-title buyers-title"><span>FOR </span><b>BUYERS</b></h2>
<svg class="abs title-wave" style="top:1440px" viewBox="0 0 88 20"><path d="M2 12 C22 2 44 4 60 8 C70 10 80 9 86 5" fill="none" stroke="var(--blue)" stroke-width="3"/><path d="M8 17 C28 9 48 11 62 14 C72 15 80 14 84 12" fill="none" stroke="var(--blue-mid)" stroke-width="2"/></svg>
<p class="abs body-copy buyers-copy">If you are in the market to buy a house, you are in the right place. Your dream house is waiting and we can help you get it. We can help you find the perfect home within your budget. We'll walk you through the entire process, from qualifying to the close of escrow.</p>

<h3 class="abs process-title buyers-process-title"><span>BUYING </span><b>PROCESS</b></h3>
<div class="abs photo-circle buyers-photo" role="img" aria-label="Young couple reviewing documents with a real estate agent"></div>

<div class="abs step-line" style="left:687px;top:1656px;height:466px"></div>
<div class="buyers-steps">
  <span class="step-dot" style="left:681px;top:1650px"></span><span class="step-icon" style="left:730px;top:1626px"><svg width="30" height="30"><circle cx="15" cy="15" r="10" fill="none" stroke="#fff" stroke-width="1.8"/><path d="M10 15l4 4 7-8" fill="none" stroke="#fff" stroke-width="1.8"/></svg></span><span class="step-label" style="left:807px;top:1645px">1. GET PRE-QUALIFIED</span>
  <span class="step-dot" style="left:681px;top:1728px"></span><span class="step-icon" style="left:730px;top:1704px"><svg width="30" height="30"><path d="M8 9h14M8 15h14M8 21h10" stroke="#fff" stroke-width="1.8"/></svg></span><span class="step-label" style="left:807px;top:1723px">2. LIST YOUR PRIORITIES</span>
  <span class="step-dot" style="left:681px;top:1805px"></span><span class="step-icon" style="left:730px;top:1781px"><svg width="30" height="30"><rect x="6" y="8" width="18" height="15" fill="none" stroke="#fff" stroke-width="1.8"/><path d="M6 13h18" stroke="#fff" stroke-width="1.8"/></svg></span><span class="step-label" style="left:807px;top:1800px">3. SHOP AROUND</span>
  <span class="step-dot" style="left:681px;top:1881px"></span><span class="step-icon" style="left:730px;top:1857px"><svg width="30" height="30"><path d="M5 15L15 6l10 9M8 13v11h14V13" fill="none" stroke="#fff" stroke-width="1.8"/></svg></span><span class="step-label" style="left:807px;top:1876px">4. PROPERTY VISITS</span>
  <span class="step-dot" style="left:681px;top:1959px"></span><span class="step-icon" style="left:730px;top:1935px"><svg width="30" height="30"><path d="M5 15L15 6l10 9M8 13v11h14V13" fill="none" stroke="#fff" stroke-width="1.8"/><path d="M12 21l6-6" stroke="#fff" stroke-width="1.6"/></svg></span><span class="step-label" style="left:807px;top:1954px">5. MAKE AN OFFER</span>
  <span class="step-dot" style="left:681px;top:2036px"></span><span class="step-icon" style="left:730px;top:2012px"><svg width="30" height="30"><circle cx="13" cy="13" r="6" fill="none" stroke="#fff" stroke-width="1.8"/><path d="M17.5 17.5L24 24" stroke="#fff" stroke-width="2"/></svg></span><span class="step-label" style="left:807px;top:2031px">6. PROPERTY INSPECTION</span>
  <span class="step-dot" style="left:681px;top:2116px"></span><span class="step-icon" style="left:730px;top:2092px"><svg width="30" height="30"><path d="M15 5L6 14h18z" fill="none" stroke="#fff" stroke-width="1.6"/><rect x="5" y="14" width="20" height="10" rx="1" fill="none" stroke="#fff" stroke-width="1.6"/></svg></span><span class="step-label" style="left:807px;top:2111px">7. CLOSE OF ESCROW</span>
</div>

<a class="abs btn btn-outline buyers-more">Learn More <svg width="8" height="10" viewBox="0 0 8 10"><path d="M2 1l4 4-4 4" fill="none" stroke="var(--blue)" stroke-width="1.6"/></svg></a>

<section class="abs sellers-band"></section>
<h2 class="abs section-title sellers-title"><span>FOR </span><b>SELLERS</b></h2>
<svg class="abs title-wave" style="top:2444px" viewBox="0 0 88 20"><path d="M2 12 C22 2 44 4 60 8 C70 10 80 9 86 5" fill="none" stroke="var(--blue)" stroke-width="3"/><path d="M8 17 C28 9 48 11 62 14 C72 15 80 14 84 12" fill="none" stroke="var(--blue-mid)" stroke-width="2"/></svg>
<p class="abs body-copy sellers-copy">If you are considering selling your house, are in the right place. We will perform a comprehensive market analysis of your property and make recommendations to make your home more attractive to potential buyers. To start this process, please complete the form below and a representative will contact you soon.</p>

<h3 class="abs process-title sellers-process-title"><span>SELLING </span><b>PROCESS</b></h3>
<div class="abs photo-circle sellers-photo" role="img" aria-label="Couple shaking hands with an agent in front of a house gate"></div>

<div class="abs step-line" style="left:167px;top:2669px;height:466px"></div>
<div class="sellers-steps">
  <span class="step-dot" style="left:161px;top:2663px"></span><span class="step-icon" style="left:211px;top:2639px"><svg width="30" height="30"><circle cx="15" cy="11" r="4" fill="none" stroke="#fff" stroke-width="1.8"/><path d="M7 24c1-5 5-7 8-7s7 2 8 7" fill="none" stroke="#fff" stroke-width="1.8"/></svg></span><span class="step-label" style="left:289px;top:2658px">1. MEET AGENT</span>
  <span class="step-dot" style="left:161px;top:2740px"></span><span class="step-icon" style="left:211px;top:2716px"><svg width="30" height="30"><rect x="8" y="5" width="14" height="20" fill="none" stroke="#fff" stroke-width="1.8"/><path d="M11 11h8M11 15h8M11 19h5" stroke="#fff" stroke-width="1.5"/></svg></span><span class="step-label" style="left:289px;top:2735px">2. LISTING AGREEMENT</span>
  <span class="step-dot" style="left:161px;top:2818px"></span><span class="step-icon" style="left:211px;top:2794px"><svg width="30" height="30"><path d="M5 15L15 6l10 9M8 13v11h14V13" fill="none" stroke="#fff" stroke-width="1.8"/></svg></span><span class="step-label" style="left:289px;top:2813px">3. PREPARE THE PROPERTY</span>
  <span class="step-dot" style="left:161px;top:2894px"></span><span class="step-icon" style="left:211px;top:2870px"><svg width="30" height="30"><path d="M5 22l7-7 4 4 9-9" fill="none" stroke="#fff" stroke-width="1.8"/></svg></span><span class="step-label" style="left:289px;top:2889px">4. MARKETING</span>
  <span class="step-dot" style="left:161px;top:2972px"></span><span class="step-icon" style="left:211px;top:2948px"><svg width="30" height="30"><circle cx="15" cy="15" r="9" fill="none" stroke="#fff" stroke-width="1.8"/><path d="M15 9v12M12 12h5a2 2 0 010 4h-4a2 2 0 000 4h5" fill="none" stroke="#fff" stroke-width="1.4"/></svg></span><span class="step-label" style="left:289px;top:2967px">5. EVALUATING OFFERS</span>
  <span class="step-dot" style="left:161px;top:3049px"></span><span class="step-icon" style="left:211px;top:3025px"><svg width="30" height="30"><rect x="8" y="5" width="14" height="20" fill="none" stroke="#fff" stroke-width="1.8"/><path d="M11 12l3 3 5-6" fill="none" stroke="#fff" stroke-width="1.5"/></svg></span><span class="step-label" style="left:289px;top:3044px">6. DISCLOSURES</span>
  <span class="step-dot" style="left:161px;top:3129px"></span><span class="step-icon" style="left:211px;top:3105px"><svg width="30" height="30"><path d="M15 5L6 14h18z" fill="none" stroke="#fff" stroke-width="1.6"/><rect x="5" y="14" width="20" height="10" rx="1" fill="none" stroke="#fff" stroke-width="1.6"/></svg></span><span class="step-label" style="left:289px;top:3124px">7. CLOSE OF ESCROW</span>
</div>

<a class="abs btn btn-outline sellers-more">Learn More <svg width="8" height="10" viewBox="0 0 8 10"><path d="M2 1l4 4-4 4" fill="none" stroke="var(--blue)" stroke-width="1.6"/></svg></a>

<section class="abs contact-band" role="img" aria-label="Golden Gate Bridge at dusk behind a dark overlay"></section>
<h2 class="abs contact-heading reply-heading"><span>LEAVE A </span><b>REPLY</b></h2>
<p class="abs reply-note">Your email address will not be published.</p>
<div class="abs field field-name">Name*</div>
<div class="abs field field-email">Email*</div>
<div class="abs field field-phone">Phone*</div>
<div class="abs field field-message">Message*</div>
<a class="abs btn btn-submit">Submit <svg width="8" height="10" viewBox="0 0 8 10"><path d="M2 1l4 4-4 4" fill="none" stroke="#fff" stroke-width="1.6"/></svg></a>

<h2 class="abs contact-heading us-heading"><span>CONTACT </span><b>US</b></h2>
<div class="abs contact-line contact-address"><svg width="14" height="20" viewBox="0 0 14 20" style="margin-top:4px"><path d="M7 1a6 6 0 016 6c0 4.5-6 12-6 12S1 11.5 1 7a6 6 0 016-6z" fill="#fff"/><circle cx="7" cy="7" r="2.3" fill="#3a3a3e"/></svg><span>4820 Larkhaven Ave.<br>Northridge CA 91330</span></div>
<div class="abs contact-line contact-phone"><svg width="16" height="16" viewBox="0 0 16 16" style="margin-top:3px"><path d="M3 1l3 3-2 2c1 2 3 4 5 5l2-2 3 3-2 3C6 15 1 10 1 3z" fill="#fff"/></svg><span>818.555.0192</span></div>
<div class="abs contact-line contact-email"><svg width="16" height="12" viewBox="0 0 16 12" style="margin-top:6px"><rect width="16" height="12" rx="1" fill="#fff"/><path d="M1 1l7 6 7-6" fill="none" stroke="#3a3a3e" stroke-width="1.3"/></svg><span>hello@brenwickhomes.com</span></div>
<div class="abs map-frame" role="img" aria-label="Street map of the greater Los Angeles area with office location pins"></div>

<svg class="abs contact-wave" viewBox="0 0 1200 150" preserveAspectRatio="none">
  <path d="M0 0 C180 110 430 150 700 110 C900 80 1060 50 1200 80 L1200 150 L0 150 Z" fill="var(--blue)"/>
  <path d="M0 40 C200 150 460 170 720 135 C920 105 1070 85 1200 110 L1200 150 L0 150 Z" fill="#fff"/>
</svg>

<footer class="abs site-footer" role="img" aria-label="Faint beach scene with palm trees and a pier"></footer>
<div class="abs brand footer-brand"><span class="brand-dot"></span><span class="brand-name">BRENWICK HOMES REALTY</span></div>
<p class="abs footer-tag">Family Owned Business Since 2006.</p>
<p class="abs footer-legal">Brenwick Homes Realty, founded in 2006, is licensed in California by the Department of Real Estate, license #01739254, and it is a DBA of Halvorsen Realty Group, Inc. CA License #02046813. All information here provided is for basic knowledge to prospects purchasing or selling real estate properties in California and not intended to be used for any other purpose.</p>
<nav class="footer-links">
  <a class="active" style="left:694px;top:4105px">Home</a>
  <a style="left:694px;top:4133px">About Us</a>
  <a style="left:694px;top:4161px">For Buyers</a>
  <a style="left:694px;top:4188px">For Sellers</a>
  <a style="left:694px;top:4217px">Contact Us</a>
  <a style="left:854px;top:4105px">Terminology</a>
  <a style="left:854px;top:4133px">Process Of Purchase</a>
  <a style="left:854px;top:4161px">Process Of Selling</a>
</nav>
<p class="abs copyright">Copyright © 2023. All rights reserved. Equal Housing Opportunity</p>
<p class="abs legal-links">Terms &amp; Conditions &nbsp;|&nbsp; Privacy Policy</p>

</body>
</html>
```